Business card for communications

Need a business card for my consulting business - I work with not for profits, start ups and social enterprises on their media, communications campaigns.

Please see my website for colours, images and fonts www.morvenquillet.example

Morven Quillet
Communications & Campaign strategist
Sydney - Melbourne
M: 0498 317 250
E: morven@morvenquillet.example
S: morvenquillet
W: morvenquillet.example
T: @morvenquillet

(above is info only and can be presented any way e.g. should not have to be M for mobile - it should be an icon)
Updates

Dear designers I have updated the brief and uploaded high res images from my website for you to use. The designs so far with the use of images and icons are much better so far. Thank you I look forward to receiving your revised designs. Morven Quillet

Industry/Entity Type

Communications

Font styles to use
Sans Serif

Requirements
Must have
• Icons for contact details
Images from the website www.morvenquillet.example
Nice to have
• Images - attached

```html
<!DOCTYPE html>
<html lang="en">
<head>
<meta charset="utf-8">
<title>Morven Quillet — Business Card</title>
<link rel="stylesheet" href="https://fonts.googleapis.com/css2?family=Archivo+Black&family=Varela+Round&display=swap">
<style>
  :root {
    --page: #e6e6e4;
    --card-yellow: #f8d210;
    --band-cream: #fbf0c4;
    --band-fade: rgba(251, 240, 196, 0);
    --label-brown: #6b5a2c;
    --contact-white: #ffffff;
    --icon-ring: #ffffff;
    --icon-ink: #3a3320;
    --icon-fill: #f3c51a;
    --name-ink: #5d5446;
    --tagline-ink: #5a4b1e;
  }
  * { box-sizing: border-box; margin: 0; padding: 0; }
  html, body {
    width: 1200px; height: 900px; overflow: hidden;
    background: var(--page);
    font-family: "Varela Round", Arial, sans-serif;
  }
  .sheet { position: relative; width: 1200px; height: 900px; }

  .card {
    position: absolute; left: 240px; width: 720px; height: 400px;
    background: var(--card-yellow);
    box-shadow: 0 6px 18px rgba(0,0,0,0.18);
    overflow: hidden;
  }
  .card--services { top: 40px; }
  .card--identity { top: 460px; }

  /* Services side */
  .service-band {
    position: absolute; left: 40px; top: 95px; width: 660px; height: 130px;
    background: linear-gradient(90deg, var(--band-cream) 0%, var(--band-cream) 70%, var(--band-fade) 100%);
    box-shadow: 0 3px 6px rgba(0,0,0,0.15);
  }
  .service { position: absolute; width: 200px; text-align: center; }
  .service__icon {
    display: block; margin: 0 auto; width: 56px; height: 56px; border-radius: 50%;
    background: var(--icon-ring);
    box-shadow: 0 2px 5px rgba(0,0,0,0.25);
  }
  .service__label {
    display: block; font-size: 16px; color: var(--label-brown); letter-spacing: -0.2px;
    white-space: nowrap;
    text-shadow: 0 1px 1px rgba(255,255,255,0.6);
  }
  .service--strategy { left: 60px; top: 160px; }
  .service--media { left: 210px; top: 110px; }
  .service--pr { left: 360px; top: 150px; }
  .service--counsel { left: 500px; top: 70px; }
  .service--media .service__label,
  .service--counsel .service__label { margin-bottom: 6px; }
  .service--strategy .service__label,
  .service--pr .service__label { margin-top: 4px; }

  .contact {
    position: absolute; display: flex; align-items: center; gap: 6px;
    color: var(--contact-white); font-size: 16px;
    text-shadow: 0 1px 2px rgba(0,0,0,0.25);
    white-space: nowrap;
  }
  .contact svg { width: 16px; height: 16px; flex: none; }
  .contact__mark { width: 15px; height: 15px; background: var(--contact-white); flex: none; }
  .contact__mark--square { border-radius: 2px; }
  .contact__mark--circle { border-radius: 50%; }
  .contact--phone { left: 34px; top: 334px; }
  .contact--email { left: 172px; top: 304px; }
  .contact--web { left: 172px; top: 346px; }
  .contact--handle { left: 484px; top: 272px; }
  .contact--chat { left: 484px; top: 312px; }

  /* Identity side */
  .name-band {
    position: absolute; left: 130px; top: 150px; width: 590px; height: 100px;
    background: linear-gradient(90deg, var(--band-cream) 0%, var(--band-cream) 75%, var(--band-fade) 100%);
  }
  .name {
    position: absolute; left: 146px; top: 168px;
    font-family: "Archivo Black", Arial, sans-serif; font-weight: 400;
    font-size: 46px; line-height: 1; letter-spacing: 1px; color: var(--name-ink);
    text-transform: uppercase; white-space: nowrap;
  }
  .tagline {
    position: absolute; right: 34px; top: 228px;
    font-size: 20px; color: var(--tagline-ink); white-space: nowrap;
    text-shadow: 0 0 6px rgba(255,255,255,0.7);
  }
</style>
</head>
<body>
<main class="sheet">

  <section class="card card--services" aria-label="Card back: services and contact">
    <div class="service-band"></div>

    <div class="service service--strategy">
      <svg class="service__icon" viewBox="0 0 56 56" aria-hidden="true">
        <circle cx="28" cy="28" r="28" fill="var(--icon-ring)"/>
        <rect x="14" y="25" width="28" height="7" rx="1" transform="rotate(45 28 28)" fill="var(--icon-fill)" stroke="var(--icon-ink)" stroke-width="1.5"/>
        <path d="M18 38 L34 16 L39 20 L23 42 L17 44 Z" fill="var(--icon-fill)" stroke="var(--icon-ink)" stroke-width="1.5" stroke-linejoin="round"/>
      </svg>
      <span class="service__label">Communications Strategy</span>
    </div>

    <div class="service service--media">
      <span class="service__label">Media Relations</span>
      <svg class="service__icon" viewBox="0 0 56 56" aria-hidden="true">
        <circle cx="28" cy="28" r="28" fill="var(--icon-ring)"/>
        <rect x="20" y="13" width="16" height="12" fill="#fff" stroke="var(--icon-ink)" stroke-width="1.5"/>
        <rect x="13" y="24" width="30" height="18" rx="2" fill="var(--icon-fill)" stroke="var(--icon-ink)" stroke-width="1.5"/>
        <path d="M18 30h20M18 34h20M22 38h12" stroke="var(--icon-ink)" stroke-width="1.5"/>
      </svg>
    </div>

    <div class="service service--pr">
      <svg class="service__icon" viewBox="0 0 56 56" aria-hidden="true">
        <circle cx="28" cy="28" r="28" fill="var(--icon-ring)"/>
        <path d="M14 20h10l3 3h13v16H14Z" fill="#fff" stroke="var(--icon-ink)" stroke-width="1.5"/>
        <path d="M17 24h10l3 3h13v15H17Z" fill="var(--icon-fill)" stroke="var(--icon-ink)" stroke-width="1.5"/>
      </svg>
      <span class="service__label">PR &amp; Campaigns</span>
    </div>

    <div class="service service--counsel">
      <span class="service__label">Strategic Counsel</span>
      <svg class="service__icon" viewBox="0 0 56 56" aria-hidden="true">
        <circle cx="28" cy="28" r="28" fill="var(--icon-ring)"/>
        <path d="M28 13a10 10 0 0 0-6 18v4h12v-4a10 10 0 0 0-6-18Z" fill="var(--icon-fill)" stroke="var(--icon-ink)" stroke-width="1.5"/>
        <path d="M23 38h10M24 41h8" stroke="var(--icon-ink)" stroke-width="1.8"/>
        <path d="M26 35v-8l2 2 2-2v8" fill="none" stroke="var(--icon-ink)" stroke-width="1.2"/>
      </svg>
    </div>

    <p class="contact contact--phone">
      <svg viewBox="0 0 24 24" aria-hidden="true"><path d="M6.6 2.5l3 3.2-1.8 2.4a13 13 0 0 0 8.1 8.1l2.4-1.8 3.2 3-2 3.1C10.5 20.8 3.2 13.5 3.5 4.5Z" fill="var(--contact-white)"/></svg>
      <span>0498 317 250</span>
    </p>
    <p class="contact contact--email">
      <svg viewBox="0 0 24 24" aria-hidden="true"><rect x="2" y="5" width="20" height="14" fill="none" stroke="var(--contact-white)" stroke-width="2"/><path d="M2 5l10 8 10-8" fill="none" stroke="var(--contact-white)" stroke-width="2"/></svg>
      <span>morven@morvenquillet.example</span>
    </p>
    <p class="contact contact--web">
      <svg viewBox="0 0 24 24" aria-hidden="true"><circle cx="12" cy="12" r="9.5" fill="none" stroke="var(--contact-white)" stroke-width="2"/><path d="M2.5 12h19M12 2.5c-5 5-5 14 0 19M12 2.5c5 5 5 14 0 19M4.5 7h15M4.5 17h15" fill="none" stroke="var(--contact-white)" stroke-width="1.5"/></svg>
      <span>www.morvenquillet.example</span>
    </p>
    <p class="contact contact--handle">
      <span class="contact__mark contact__mark--square"></span>
      <span>@morvenquillet</span>
    </p>
    <p class="contact contact--chat">
      <span class="contact__mark contact__mark--circle"></span>
      <span>morvenquillet</span>
    </p>
  </section>

  <section class="card card--identity" aria-label="Card front: name and title">
    <div class="name-band"></div>
    <h1 class="name">Morven Quillet</h1>
    <p class="tagline">Communications &amp; Campaign strategist</p>
  </section>

</main>
</body>
</html>
```